Etiketten-Design für Kauartikel
Zielgruppe
Wir wünschen uns ein neues Etikett für unsere Kauartikel.
Als Essener Manufaktur spezialisierten wir uns voll auf die ganzheitliche, artgerechte und getreidefreie Nahrung für Hunde und Katzen. In unseren eigenen 2 Filialen setzen wir uns seit Jahren täglich mit Theorie und Praxis dieser Verpflegung zum leiblichen Wohlbefinden unserer „vierbeinigen Freunde” auseinander. Unserer eigenen Devise folgend „besser geht immer“ hat es uns nicht ausgereicht, einfach „nur“ 2 Einzelhandelsfilialen unser Eigen zu nennen. Daher sind wir einen Schritt weiter gegangen und haben die Zulassung als Futtermittelhersteller durchlaufen.
Unsere Zulassung umfasst aktuell die Herstellung/Konfektionierung von
• Nahrungsergänzungen (pflanzlicher und tiersicher Herkunft)
• Gemüse (pflanzlicher Herkunft)
• Öle (pflanzlicher Herkunft)
• Kauartikel (pflanzlicher und tiersicher Herkunft)
Der wichtigste Pfeiler unseres Sortiments ist das Thema BARF (Biologisch Artgerechtes Rohes Futter) und eine sehr ausgeprägte Beratungsqualität. Auch wenn wir biozertifiziert für pflanzliche Öle sind, steht das „biologisch“ beim Wording BARF nicht für Bio-Produkte, sondern frei formuliert für das Schlagwort „an die Natur angelehnt“. BARF wiederum beinhaltet somit rohes Futter, bestehend aus Fleisch und Gemüse, ergänzt mit sinnvollen Nahrungsergänzungen.
Da wir mit dem Thema Ernährung nicht dogmatisch umgehen, haben wir für unsere Kunden ebenfalls alternative Fütterungsformen wie z.B. Dosenfleisch und Trockenfutter in hoher Qualität im Sortiment. Das Angebot wird abgerundet durch feine Kauartikel die selbstverständlich nicht chemisch behandelt oder bestrahlt sind, hochwertige Nahrungsergänzungen und Öle, größtenteils in Lebensmittel- bzw. Bioqualität, runden das Sortiment ab.
Sämtliche Nahrungsergänzungen, pflanzliche Bio-Öle, Kauartikel und Gemüsemischungen werden von uns sorgf..
Aufgabenstellung
Lassen Sie Ihrer Kreativität freien Lauf.

```html
<!DOCTYPE html>
<html lang="de">
<head>
<meta charset="utf-8">
<title>Nachtpfote Kauartikel – Etiketten</title>
<link href="https://fonts.googleapis.com/css2?family=Oswald:wght@300;400;500;600&display=swap" rel="stylesheet">
<style>
  :root {
    --stage: #575757;
    --ink: #272727;
    --wine: #9b1b2e;
    --moon: #f7f3d2;
    --panel: #ffffff;
    --arc: #5c5c5c;
    --sage: #bfcbc2;
    --cream: #fdfbe0;
    --white: #ffffff;
    --stone: #a0a0a0;
    --silhouette: #2a2a2a;
  }
  * { box-sizing: border-box; margin: 0; padding: 0; }
  html, body { width: 1200px; height: 1200px; overflow: hidden; }
  body { background: var(--stage); font-family: "Oswald", sans-serif; color: var(--ink); position: relative; }

  .label { position: absolute; width: 450px; height: 492px; overflow: hidden; border-radius: 3px; }
  .label--sage { left: 119px; top: 84px; background: var(--sage); }
  .label--cream { left: 632px; top: 82px; background: var(--cream); }
  .label--white { left: 120px; top: 631px; background: var(--white); }
  .label--stone { left: 633px; top: 629px; background: var(--stone); }

  .brand-moon { position: absolute; left: 43px; top: 9px; width: 120px; height: 120px; border-radius: 50%; background: var(--moon); }
  .brand-name { position: absolute; left: 140px; top: 18px; font-weight: 600; font-size: 46px; line-height: 1; letter-spacing: 0.5px; color: var(--ink); }
  .brand-line { position: absolute; right: 54px; top: 80px; font-weight: 500; font-size: 26px; line-height: 1; color: var(--ink); }

  .panel { position: absolute; left: 25px; top: 114px; width: 402px; height: 321px; background: var(--panel); border-radius: 30px; }
  .panel-arcs { position: absolute; left: 0; top: 0; width: 402px; height: 321px; }

  .title { position: absolute; font-weight: 600; line-height: 0.95; color: var(--ink); text-transform: uppercase; letter-spacing: -0.5px; }
  .title--single { left: 0; width: 402px; top: 34px; text-align: center; font-size: 62px; }
  .subtitle { position: absolute; font-weight: 300; color: var(--ink); line-height: 1; }
  .weight { position: absolute; font-weight: 500; font-size: 21px; line-height: 1; color: var(--ink); }

  .animal { position: absolute; background: var(--silhouette); border-radius: 45% 45% 8px 8px; }
  .ground { position: absolute; height: 1px; background: var(--ink); }

  .quality-tab { position: absolute; left: 162px; top: 226px; width: 242px; height: 45px; background: var(--wine); border-radius: 22px 0 0 22px; color: #fff; font-weight: 300; font-size: 27px; letter-spacing: 3px; word-spacing: 8px; line-height: 45px; text-align: center; }

  .web { position: absolute; left: 0; width: 402px; top: 280px; text-align: center; font-weight: 500; font-size: 27px; line-height: 1; color: var(--ink); }

  .footer { position: absolute; left: 0; width: 450px; text-align: center; color: var(--ink); line-height: 1; }
  .footer-claim { top: 440px; font-size: 13px; font-weight: 500; }
  .footer-small { font-size: 7.5px; font-weight: 400; }
  .footer-small.l1 { top: 458px; }
  .footer-small.l2 { top: 470px; }
  .footer-small.l3 { top: 482px; }
</style>
</head>
<body>

<svg width="0" height="0" style="position:absolute">
  <defs>
    <g id="panel-arcs" fill="none" stroke="var(--arc)" stroke-width="2.5" stroke-linecap="round">
      <path d="M28 14 Q16 18 14 30"/>
      <path d="M374 14 Q386 18 388 30"/>
      <path d="M14 291 Q16 303 28 307"/>
      <path d="M388 291 Q386 303 374 307"/>
    </g>
  </defs>
</svg>

<!-- Entenflügel -->
<section class="label label--sage">
  <div class="brand-moon"></div>
  <div class="brand-name">NACHTPFOTE</div>
  <div class="brand-line">KAUARTIKEL</div>
  <div class="panel">
    <svg class="panel-arcs" viewBox="0 0 402 321"><use href="#panel-arcs"/></svg>
    <h2 class="title title--single">Entenflügel</h2>
    <div class="animal" role="img" aria-label="Silhouette einer Ente" style="left:35px;top:113px;width:141px;height:141px;"></div>
    <div class="ground" style="left:25px;top:255px;width:145px;"></div>
    <div class="quality-tab">FINEST QUALITY</div>
    <div class="web">www.nachtpfote-snacks.com</div>
  </div>
  <p class="footer footer-claim">Frei von künstlichen Farb-, Konservierungs- und Aromastoffen</p>
  <p class="footer footer-small l1">Nachtpfote GmbH | Lindenweg 12 | 45100 Musterstadt | www.nachtpfote.de |</p>
  <p class="footer footer-small l2">hallo@nachtpfote.de | +49 (0) 200 – 12 34 56 78</p>
  <p class="footer footer-small l3">Futtermittelhersteller- Nr.: DE 00 000 123 45</p>
</section>

<!-- Kälbernasen -->
<section class="label label--cream">
  <div class="brand-moon"></div>
  <div class="brand-name">NACHTPFOTE</div>
  <div class="brand-line">KAUARTIKEL</div>
  <div class="panel">
    <svg class="panel-arcs" viewBox="0 0 402 321"><use href="#panel-arcs"/></svg>
    <h2 class="title title--single">Kälbernasen</h2>
    <div class="animal" role="img" aria-label="Silhouette eines Kalbes" style="left:30px;top:132px;width:160px;height:123px;border-radius:30% 40% 6px 6px;"></div>
    <div class="ground" style="left:18px;top:256px;width:150px;"></div>
    <div class="quality-tab">FINEST QUALITY</div>
    <div class="web">www.nachtpfote-snacks.com</div>
  </div>
  <p class="footer footer-claim">Frei von künstlichen Farb-, Konservierungs- und Aromastoffen</p>
  <p class="footer footer-small l1">Nachtpfote GmbH | Lindenweg 12 | 45100 Musterstadt | www.nachtpfote.de |</p>
  <p class="footer footer-small l2">hallo@nachtpfote.de | +49 (0) 200 – 12 34 56 78</p>
  <p class="footer footer-small l3">Futtermittelhersteller- Nr.: DE 00 000 123 45</p>
</section>

<!-- Hühnerherzen -->
<section class="label label--white">
  <div class="brand-moon"></div>
  <div class="brand-name">NACHTPFOTE</div>
  <div class="brand-line">KAUARTIKEL</div>
  <div class="panel" style="border:0;">
    <svg class="panel-arcs" viewBox="0 0 402 321"><use href="#panel-arcs"/></svg>
    <h2 class="title" style="left:155px;top:37px;font-size:64px;">Hühner-<br>Herzen</h2>
    <p class="subtitle" style="left:170px;top:162px;font-size:23px;">GEFRIERGETROCKNET</p>
    <p class="weight" style="left:332px;top:203px;">100 G</p>
    <div class="animal" role="img" aria-label="Silhouette eines Hahns" style="left:10px;top:106px;width:145px;height:150px;"></div>
    <div class="ground" style="left:5px;top:257px;width:175px;"></div>
    <div class="quality-tab">FINEST QUALITY</div>
    <div class="web">www.nachtpfote-snacks.com</div>
  </div>
  <p class="footer footer-claim">Frei von künstlichen Farb-, Konservierungs- und Aromastoffen</p>
  <p class="footer footer-small l1">Nachtpfote GmbH | Lindenweg 12 | 45100 Musterstadt | www.nachtpfote.de |</p>
  <p class="footer footer-small l2">hallo@nachtpfote.de | +49 (0) 200 – 12 34 56 78</p>
  <p class="footer footer-small l3">Futtermittelhersteller- Nr.: DE 00 000 123 45</p>
</section>

<!-- Kaninchenohren -->
<section class="label label--stone">
  <div class="brand-moon"></div>
  <div class="brand-name">NACHTPFOTE</div>
  <div class="brand-line">KAUARTIKEL</div>
  <div class="panel">
    <svg class="panel-arcs" viewBox="0 0 402 321"><use href="#panel-arcs"/></svg>
    <h2 class="title" style="left:76px;top:28px;font-size:64px;text-align:right;">Kaninchen-<br>Ohren</h2>
    <p class="subtitle" style="left:200px;top:158px;font-size:34px;">MIT FELL</p>
    <p class="weight" style="left:340px;top:205px;">500G</p>
    <div class="animal" role="img" aria-label="Silhouette eines Kaninchens" style="left:15px;top:136px;width:140px;height:134px;"></div>
    <div class="ground" style="left:0;top:270px;width:170px;"></div>
    <div class="quality-tab">FINEST QUALITY</div>
    <div class="web">www.nachtpfote-snacks.com</div>
  </div>
  <p class="footer footer-claim">Frei von künstlichen Farb-, Konservierungs- und Aromastoffen</p>
  <p class="footer footer-small l1">Nachtpfote GmbH | Lindenweg 12 | 45100 Musterstadt | www.nachtpfote.de |</p>
  <p class="footer footer-small l2">hallo@nachtpfote.de | +49 (0) 200 – 12 34 56 78</p>
  <p class="footer footer-small l3">Futtermittelhersteller- Nr.: DE 00 000 123 45</p>
</section>

</body>
</html>
```